Vorlund Business Card Design Needed

We are a consultation firm called "Vorlund Inc" or simply Vorlund. Would would like a simple card utilizing the blue and grays in our logo (perhaps even different shades and hues of blue). Logo and Initials of Card holder one side and information on the other.

Target Market(s)

We are B 2 B company. We deal mostly with upper management.

Industry/Entity Type

Business

Contact Information for Business Card

Name. Title. phone. email. website.

```html
<!DOCTYPE html>
<html lang="en">
<head>
<meta charset="utf-8">
<title>Vorlund Inc — Business Card</title>
<link href="https://fonts.googleapis.com/css2?family=Michroma&family=Open+Sans:wght@300;400&display=swap" rel="stylesheet">
<style>
  :root {
    --backdrop: #121314;
    --paper-white: #f1f2f3;
    --paper-shade: #d9dbdd;
    --card-dark: #1f2021;
    --card-dark-edge: #2c2d2f;
    --brand-blue: #4aa3dc;
    --stripe-blue: #0f79a8;
    --stripe-gray: #7b7c7e;
    --ink-light: #e6e7e8;
    --ink-soft: #b9bbbd;
    --mark-gray: #c9cbcd;
  }
  html, body {
    margin: 0;
    padding: 0;
    width: 1200px;
    height: 871px;
    overflow: hidden;
    background: var(--backdrop);
  }
  .canvas {
    position: relative;
    width: 1200px;
    height: 871px;
    background: var(--backdrop);
  }
  .card {
    position: absolute;
    width: 600px;
    height: 343px;
    box-sizing: border-box;
  }
  /* Front: white logo side */
  .card-front {
    left: 90px;
    top: 70px;
    background: linear-gradient(135deg, var(--paper-white), var(--paper-shade));
    display: flex;
    align-items: center;
    justify-content: center;
    gap: 26px;
  }
  .brand-mark {
    width: 92px;
    height: 92px;
    border-radius: 50%;
    border: 5px solid var(--brand-blue);
    box-sizing: border-box;
  }
  .brand-name {
    font-family: "Michroma", sans-serif;
    font-size: 34px;
    letter-spacing: 4px;
    color: var(--brand-blue);
    text-transform: uppercase;
  }
  /* Back: dark information side */
  .card-back {
    left: 510px;
    top: 458px;
    background: linear-gradient(160deg, var(--card-dark-edge), var(--card-dark) 55%);
    overflow: hidden;
  }
  .card-back .logo-block {
    position: absolute;
    left: 44px;
    top: 60px;
    display: flex;
    flex-direction: column;
    align-items: flex-start;
    gap: 18px;
  }
  .card-back .brand-mark {
    width: 110px;
    height: 110px;
    border-color: var(--mark-gray);
  }
  .card-back .brand-name {
    font-size: 22px;
    letter-spacing: 3px;
  }
  .holder {
    position: absolute;
    left: 300px;
    top: 70px;
  }
  .holder-name {
    font-family: "Michroma", sans-serif;
    font-size: 20px;
    color: var(--ink-light);
    letter-spacing: 1.5px;
    margin: 0;
  }
  .holder-title {
    font-family: "Michroma", sans-serif;
    font-size: 11px;
    letter-spacing: 3px;
    color: var(--ink-soft);
    text-transform: uppercase;
    margin: 6px 0 16px;
  }
  .contact-list {
    list-style: none;
    margin: 0;
    padding: 0;
  }
  .contact-item {
    display: flex;
    align-items: center;
    gap: 14px;
    font-family: "Open Sans", sans-serif;
    font-weight: 300;
    font-size: 22px;
    color: var(--ink-light);
    height: 38px;
  }
  .contact-icon {
    width: 18px;
    height: 18px;
    flex: none;
  }
  .edge-stripe {
    position: absolute;
    left: 0;
    right: 0;
    bottom: 0;
    height: 26px;
    display: flex;
  }
  .edge-stripe .stripe-gray { flex: 1; background: var(--stripe-gray); }
  .edge-stripe .stripe-blue { flex: 1.15; background: var(--stripe-blue); }
</style>
</head>
<body>
<main class="canvas">

  <section class="card card-front" aria-label="Card front">
    <div class="brand-mark"></div>
    <div class="brand-name">Vorlund Inc</div>
  </section>

  <section class="card card-back" aria-label="Card back">
    <div class="logo-block">
      <div class="brand-mark"></div>
      <div class="brand-name">Vorlund Inc</div>
    </div>

    <div class="holder">
      <p class="holder-name">Your Name</p>
      <p class="holder-title">Job Title</p>
      <ul class="contact-list">
        <li class="contact-item">
          <svg class="contact-icon" viewBox="0 0 20 20" aria-hidden="true">
            <rect x="2" y="6" width="16" height="11" rx="2" fill="none" stroke="#e6e7e8" stroke-width="1.6"/>
            <path d="M4 6 C6 2 14 2 16 6" fill="none" stroke="#e6e7e8" stroke-width="1.6"/>
            <circle cx="10" cy="11.5" r="2.6" fill="none" stroke="#e6e7e8" stroke-width="1.4"/>
          </svg>
          000-000-0000
        </li>
        <li class="contact-item">
          <svg class="contact-icon" viewBox="0 0 20 20" aria-hidden="true">
            <rect x="2" y="4.5" width="16" height="11" fill="none" stroke="#e6e7e8" stroke-width="1.6"/>
            <path d="M2 4.5 L10 11 L18 4.5" fill="none" stroke="#e6e7e8" stroke-width="1.6"/>
          </svg>
          Email@
        </li>
        <li class="contact-item">
          <svg class="contact-icon" viewBox="0 0 20 20" aria-hidden="true">
            <circle cx="10" cy="10" r="8" fill="none" stroke="#e6e7e8" stroke-width="1.4"/>
            <ellipse cx="10" cy="10" rx="3.5" ry="8" fill="none" stroke="#e6e7e8" stroke-width="1.2"/>
            <path d="M2 10 H18 M3.5 6 H16.5 M3.5 14 H16.5" stroke="#e6e7e8" stroke-width="1.1"/>
          </svg>
          website
        </li>
      </ul>
    </div>

    <div class="edge-stripe">
      <div class="stripe-gray"></div>
      <div class="stripe-blue"></div>
    </div>
  </section>

</main>
</body>
</html>
```